High-End audio shop owner needs a business card

I need a personal Business Card for my Audio shop which exists since 1962. We offer high Quality brands, professional Attention and run our own repair-service-department. I look for a design which will be printed on high Quality paper and shall convey trust to the Client that we are very serious. Language is german.

```html
<!DOCTYPE html>
<html lang="de">
<head>
<meta charset="utf-8">
<title>Hi-Fi Brunnmatt – Visitenkarte</title>
<link href="https://fonts.googleapis.com/css2?family=Roboto:wght@400;500;900&family=Roboto+Condensed:wght@500&display=swap" rel="stylesheet">
<style>
  :root {
    --backdrop: #3b3b3d;
    --card: #232325;
    --accent: #ff5a00;
    --text-light: #e6e6e6;
  }
  html, body {
    margin: 0;
    padding: 0;
    overflow: hidden;
  }
  body {
    width: 799px;
    height: 1200px;
    background: var(--backdrop);
    font-family: "Roboto", sans-serif;
    position: relative;
  }
  .card {
    position: absolute;
    left: 90px;
    width: 620px;
    height: 380px;
    background: var(--card);
    box-shadow: 0 14px 30px rgba(0,0,0,0.45);
    box-sizing: border-box;
  }
  .card--front { top: 130px; }
  .card--back { top: 700px; }

  .brand {
    display: flex;
    align-items: center;
    gap: 12px;
    color: var(--accent);
    font-family: "Roboto", sans-serif;
    font-weight: 900;
    text-transform: uppercase;
    white-space: nowrap;
    letter-spacing: 1px;
  }
  .brand__dot {
    background: var(--accent);
    flex: none;
  }
  .card--front .brand {
    position: absolute;
    left: 0;
    right: 0;
    top: 155px;
    justify-content: center;
    font-size: 50px;
  }
  .card--front .brand__dot { width: 18px; height: 18px; }

  .card--back .brand {
    position: absolute;
    left: 40px;
    top: 120px;
    font-size: 34px;
  }
  .card--back .brand__dot { width: 12px; height: 12px; }
  .address {
    position: absolute;
    left: 40px;
    top: 175px;
    color: var(--text-light);
    font-size: 15px;
  }

  .contact {
    position: absolute;
    left: 400px;
    top: 210px;
    color: var(--text-light);
  }
  .contact__name {
    color: var(--accent);
    font-family: "Roboto Condensed", sans-serif;
    font-weight: 500;
    font-size: 27px;
    margin: 0;
    line-height: 1.1;
  }
  .contact__role {
    font-size: 15px;
    font-weight: 500;
    margin: 2px 0 14px;
  }
  .contact__list {
    list-style: none;
    margin: 0;
    padding: 0;
    font-size: 15px;
  }
  .contact__list li {
    display: flex;
    align-items: center;
    gap: 10px;
    height: 22px;
  }
  .contact__list svg {
    width: 13px;
    height: 13px;
    fill: var(--accent);
    flex: none;
  }
</style>
</head>
<body>
  <section class="card card--front">
    <div class="brand"><span class="brand__dot"></span>Hi-Fi Brunnmatt</div>
  </section>

  <section class="card card--back">
    <div class="brand"><span class="brand__dot"></span>Hi-Fi Brunnmatt</div>
    <p class="address">Lindenweg 12 CH-3011 Bern</p>

    <div class="contact">
      <h1 class="contact__name">Lukas Brunnmatt</h1>
      <p class="contact__role">Managing Director</p>
      <ul class="contact__list">
        <li>
          <svg viewBox="0 0 16 16" aria-hidden="true"><path d="M2 5c0-2 3-3 6-3s6 1 6 3v1h-3V5H5v1H2zM3 7h10l1 7H2zM8 9a2 2 0 1 0 0 4 2 2 0 0 0 0-4z"/></svg>
          031 555 01 47
        </li>
        <li>
          <svg viewBox="0 0 16 16" aria-hidden="true"><path d="M1 3h14v10H1zM2 4l6 5 6-5v1L8 10 2 5z" fill-rule="evenodd"/></svg>
          hi@hifi-bm.ch
        </li>
        <li>
          <svg viewBox="0 0 16 16" aria-hidden="true"><path d="M8 1a7 7 0 1 0 0 14A7 7 0 0 0 8 1zm0 1.5c.8 0 1.7 1.6 2 4H6c.3-2.4 1.2-4 2-4zM5.9 7.5h4.2c0 .4 0 .7-.1 1H6c0-.3-.1-.6-.1-1zM3 7.5h1.9v1H3zm8.1 0H13v1h-1.9zM6 9.5h4c-.3 2.4-1.2 4-2 4s-1.7-1.6-2-4z"/></svg>
          www.hifi-bm.ch
        </li>
      </ul>
    </div>
  </section>
</body>
</html>
```